New website for Pollard Law Firm at www.keepwinning-example.com

We are a professional law firm located in the Nashville, Tennessee USA area. We focus on personal injury law. We are looking for a slick new website that is user friendly for updating with new blogs, videos, etc. The primary colors should be red, black, and white. It should load extremely fast and have a good mobile component. The pages for the design will include a home page, about us, news, contact us, and practice page. The practice page will be copied for all the practice areas including motor vehicle accidents, slip and fall accidents, dog bites, etc. We have included an image which we would like to include in the new site which shows the color scheme The image is called banner-Car Wreck. The new website should NOT have gavels, court houses, law books, scales or the typical images for a law firm.

Target Market(s)

People in Tennessee involved in accidents

Industry/Entity Type

Legal services, law firm

Coding

Coded - Design and coding required

Number of Pages Required

5+ page

Font styles to use
Serif

Colors
EB3D1F
EC4F4E
F09395
F8D3D4
FCEDEE

Requirements
Should not have
• Gavels, columns, scales, law related images

```html
<!DOCTYPE html>
<html lang="en">
<head>
<meta charset="utf-8">
<title>Pollard Law Firm</title>
<link href="https://fonts.googleapis.com/css2?family=EB+Garamond:wght@500;600;700&family=Poppins:wght@400;500;600&family=Oswald:wght@400;500&display=swap" rel="stylesheet">
<style>
:root{
  --red:#cf2e2e;
  --red-deep:#b82424;
  --pink:#f8d3d4;
  --blush:#fcedee;
  --ink:#1b1b1e;
  --text:#333;
  --muted:#777;
  --line:#d9d9d9;
  --white:#fff;
}
*{margin:0;padding:0;box-sizing:border-box}
html,body{width:1200px;height:4501px;overflow:hidden;background:var(--white)}
body{position:relative;font-family:'Poppins',sans-serif;color:var(--text)}
.abs{position:absolute}
.shapes{position:absolute;left:0;top:0;width:1200px;height:4501px}

/* header / hero */
.brand{position:absolute;left:61px;top:22px;display:flex;align-items:center;gap:9px;font-family:'Poppins',sans-serif;font-weight:600;font-size:19px;line-height:1;color:var(--white);white-space:nowrap}
.brand .mark{width:14px;height:14px;background:var(--red)}
.nav{position:absolute;top:24px;left:0;font-size:12px;color:var(--white)}
.nav a{position:absolute;white-space:nowrap;color:var(--white);text-decoration:none}
.nav a.active{color:var(--red)}
.btn{position:absolute;background:var(--red);color:var(--white);font-family:'Oswald',sans-serif;font-size:12px;letter-spacing:.3px;display:flex;align-items:center;justify-content:center;text-transform:uppercase}
.hero-title{position:absolute;left:61px;top:150px;font-family:'EB Garamond',serif;font-weight:700;font-size:72px;line-height:84px;color:var(--white)}
.hero-text{position:absolute;left:61px;top:332px;width:390px;font-size:13px;line-height:21px;color:#eee}
.hero-btn{left:61px;top:423px;width:142px;height:35px;border-radius:18px;font-family:'Poppins',sans-serif;font-size:12px}
.dots{position:absolute;left:1130px;top:232px;width:20px}
.dots span{position:absolute;left:6px;width:8px;height:8px;border-radius:50%;background:var(--red)}

.h2{position:absolute;left:0;width:1200px;text-align:center;font-family:'EB Garamond',serif;font-weight:500;font-size:34px;letter-spacing:1px;color:var(--ink)}

/* practice cards */
.card{position:absolute;top:782px;width:189px;height:210px;background:var(--white);box-shadow:0 2px 10px rgba(0,0,0,.12);text-align:center}
.card::before{content:"";position:absolute;left:8px;top:8px;width:189px;height:210px;background:#f1f1f1;z-index:-1;box-shadow:0 2px 8px rgba(0,0,0,.08)}
.card.featured{background:var(--red);color:var(--white)}
.card svg{margin-top:24px}
.card h3{font-family:'EB Garamond',serif;font-weight:600;font-size:18px;color:var(--ink);margin-top:6px}
.card p{font-size:12px;line-height:19px;color:var(--muted);padding:4px 14px 0}
.card.featured h3,.card.featured p{color:var(--white)}

/* about */
.about-title{position:absolute;left:61px;top:1205px;font-family:'EB Garamond',serif;font-weight:500;font-size:34px;color:var(--white);letter-spacing:1px}
.about-sub{position:absolute;left:61px;top:1256px;width:320px;font-family:'Oswald',sans-serif;font-size:16px;line-height:26px;color:var(--white)}
.about-text{position:absolute;left:61px;top:1318px;width:400px;font-size:11.5px;line-height:19.5px;color:#fde9e9}
.about-text p+p{margin-top:7px}
.read-more{position:absolute;left:89px;top:1510px;font-family:'Oswald',sans-serif;font-size:12px;color:var(--white)}
.photo{position:absolute}

/* team */
.member{position:absolute;top:1799px;width:260px;text-align:center}
.member .avatar{width:166px;height:166px;border-radius:50%;margin:0 auto}
.member h4{font-family:'EB Garamond',serif;font-weight:600;font-size:17px;color:var(--ink);margin-top:18px}
.member p{font-size:11.5px;color:var(--muted);margin-top:6px}

.quote{position:absolute;left:0;top:2248px;width:1200px;text-align:center;font-family:'Oswald',sans-serif;font-size:22px;line-height:34px;color:var(--white)}

/* testimonial */
.t-card{position:absolute;left:171px;top:2863px;width:826px;height:190px;background:var(--white);box-shadow:0 3px 14px rgba(0,0,0,.1)}
.t-name{position:absolute;left:407px;top:2906px;font-family:'EB Garamond',serif;font-weight:600;font-size:17px;color:var(--ink)}
.t-text{position:absolute;left:407px;top:2936px;width:460px;font-size:11.5px;line-height:20px;color:var(--muted)}

/* news */
.news{position:absolute;top:3251px;width:278px;height:382px;background:var(--white);box-shadow:0 3px 12px rgba(0,0,0,.15)}
.news .thumb{height:190px;border-bottom:4px solid var(--red)}
.news .date{font-size:11px;color:#999;margin:28px 17px 0}
.news h3{font-family:'EB Garamond',serif;font-weight:600;font-size:17px;line-height:24px;color:var(--red);margin:6px 17px 0}
.news p{font-size:11.5px;line-height:19px;color:var(--muted);margin:8px 17px 0}

.field{position:absolute;font-size:11px;color:#888;border-bottom:1px solid var(--line);padding-bottom:8px}

/* footer */
.f-title{position:absolute;top:4226px;font-family:'EB Garamond',serif;font-weight:600;font-size:18px;color:var(--red)}
.f-links{position:absolute;left:337px;top:4256px;list-style:none;font-size:11.5px;line-height:26px;color:#ddd}
.f-item{position:absolute;left:643px;font-size:11.5px;line-height:19px;color:#ddd}
.f-icon{position:absolute;left:612px}
.social{position:absolute;top:4259px;width:30px;height:30px;border-radius:50%;background:var(--red);border:2px solid var(--white)}
.copy{position:absolute;left:0;top:4445px;width:1200px;height:56px;background:var(--red);color:var(--white);font-size:11.5px;display:flex;align-items:center;justify-content:center}
</style>
</head>
<body>

<svg class="shapes" viewBox="0 0 1200 4501" aria-hidden="true">
  <defs>
    <linearGradient id="heroGrad" x1="0" y1="0" x2="1" y2="1">
      <stop offset="0" stop-color="#2a2326"/>
      <stop offset=".55" stop-color="#4a2f30"/>
      <stop offset="1" stop-color="#1c1b1f"/>
    </linearGradient>
    <linearGradient id="quoteGrad" x1="0" y1="0" x2="1" y2="0">
      <stop offset="0" stop-color="#1f1d20"/>
      <stop offset=".5" stop-color="#3a2a26"/>
      <stop offset="1" stop-color="#1c1b1e"/>
    </linearGradient>
  </defs>
  <path d="M0 0H1200V520Q600 740 0 520Z" fill="url(#heroGrad)"/>
  <path d="M0 1100C380 1080 800 1170 1200 1130V1330C900 1580 420 1630 0 1650Z" fill="var(--red)"/>
  <rect x="0" y="2110" width="1200" height="376" fill="url(#quoteGrad)"/>
  <path d="M0 3092Q600 3214 1200 3057V3651Q700 3493 0 3310Z" fill="var(--red)"/>
  <path d="M0 4183Q600 4080 1200 4183V4445H0Z" fill="var(--ink)"/>
</svg>

<!-- header -->
<div class="brand"><span class="mark"></span>Pollard Law Firm</div>
<nav class="nav">
  <a class="active" style="left:465px">Home</a>
  <a style="left:532px">About Us</a>
  <a style="left:618px">News</a>
  <a style="left:682px">Prectice Area</a>
  <a style="left:795px">Our Team</a>
  <a style="left:884px">Contact Us</a>
</nav>
<div class="btn" style="left:975px;top:16px;width:164px;height:36px">Book an appointment</div>

<h1 class="hero-title">Don’t Lose What’s<br>Legally Yours</h1>
<p class="hero-text">There are many law firms in Tennessee who claim to be trial lawyers, but their attorneys have never seen a courtroom.</p>
<div class="btn hero-btn">CONTACT US</div>
<div class="dots">
  <span style="top:0;left:0;width:20px;height:20px;background:none;border:1.5px solid var(--red)"></span>
  <span style="top:6px;left:6px"></span>
  <span style="top:30px;left:9.5px;width:1px;height:34px;border-radius:0"></span>
  <span style="top:84px"></span>
  <span style="top:108px"></span>
</div>

<!-- practice area -->
<h2 class="h2" style="top:692px">OUR PRACTICE AREA</h2>
<div class="card" style="left:157px">
  <svg width="60" height="60" viewBox="0 0 60 60"><circle cx="30" cy="30" r="28" fill="none" stroke="var(--red)" stroke-width="1.5"/><circle cx="30" cy="21" r="6" fill="none" stroke="var(--red)" stroke-width="1.5"/><path d="M19 44v-6a11 11 0 0 1 22 0v6" fill="none" stroke="var(--red)" stroke-width="1.5"/></svg>
  <h3>Personal Injury</h3><p>Lorem Ipsum is simply dummy text of the printing and typesetting industry.</p>
</div>
<div class="card featured" style="left:390px">
  <svg width="60" height="60" viewBox="0 0 60 60"><circle cx="30" cy="30" r="28" fill="none" stroke="#fff" stroke-width="1.5"/><path d="M16 36l4-10h20l4 10v6H16z" fill="none" stroke="#fff" stroke-width="1.5"/><circle cx="22" cy="42" r="3" fill="#fff"/><circle cx="38" cy="42" r="3" fill="#fff"/></svg>
  <h3>Vehicle accidents</h3><p>Lorem Ipsum is simply dummy text of the printing and typesetting industry.</p>
</div>
<div class="card" style="left:622px">
  <svg width="60" height="60" viewBox="0 0 60 60"><circle cx="30" cy="30" r="28" fill="none" stroke="var(--red)" stroke-width="1.5"/><circle cx="31" cy="17" r="4" fill="none" stroke="var(--red)" stroke-width="1.5"/><path d="M30 22l-4 12 6 6M26 28l-6 4M30 26l8 4M26 34l-6 10" fill="none" stroke="var(--red)" stroke-width="1.5"/></svg>
  <h3>Dog bites</h3><p>Lorem Ipsum is simply dummy text of the printing and typesetting industry.</p>
</div>
<div class="card" style="left:854px">
  <svg width="60" height="60" viewBox="0 0 60 60"><circle cx="30" cy="30" r="28" fill="none" stroke="var(--red)" stroke-width="1.5"/><circle cx="24" cy="18" r="4" fill="none" stroke="var(--red)" stroke-width="1.5"/><path d="M26 23l6 10 10 2M30 30l-10 6M14 44h32" fill="none" stroke="var(--red)" stroke-width="1.5"/></svg>
  <h3>Slip and fall</h3><p>Lorem Ipsum is simply dummy text of the printing and typesetting industry.</p>
</div>
<div class="btn" style="left:540px;top:1036px;width:120px;height:35px">View more</div>

<!-- about -->
<h2 class="about-title">ABOUT US</h2>
<div class="about-sub">WE ARE TRIAL LAWYERS AND WE ARE PROUD OF IT!</div>
<div class="about-text">
  <p>It is very hard not to take each case personally. Our clients include victims of personal injury who did not ask for the pain from a car wreck; professionals who are trying to provide for their family and save their license; and parents falsely accused in a child custody proceeding.</p>
  <p>We cannot make guarantees; however, we can assure every client that we will do everything possible to protect what is theirs.</p>
</div>
<div class="read-more">READ MORE</div>
<div class="photo" role="img" aria-label="Office team photo, blurred backdrop" style="left:688px;top:1263px;width:425px;height:323px;background:linear-gradient(135deg,#3a3d44,#9aa2ad 55%,#5b6470)"></div>
<div class="photo" style="left:655px;top:1301px;width:423px;height:355px;border:6px solid var(--red-deep)"></div>
<div class="photo" role="img" aria-label="Lawyers shaking hands with clients in a bright meeting room" style="left:638px;top:1315px;width:424px;height:323px;background:linear-gradient(135deg,#cfd4da,#8e949c 50%,#4a4d55)"></div>

<!-- team -->
<h2 class="h2" style="top:1727px">OUR PRACTICE AREA</h2>
<div class="member" style="left:184px"><div class="avatar" role="img" aria-label="Portrait of attorney Alan Brooks" style="background:radial-gradient(circle at 50% 40%,#d9d3cd,#8b8f96)"></div><h4>Alan Brooks</h4><p>Order of the Barristers</p></div>
<div class="member" style="left:470px"><div class="avatar" role="img" aria-label="Portrait of paralegal Owen Hartley" style="background:radial-gradient(circle at 50% 40%,#a06a4c,#3d2a22);box-shadow:0 5px 0 var(--red)"></div><h4 style="margin-top:16px">Owen Hartley</h4><p>Litigation Paralegal</p></div>
<div class="member" style="left:762px"><div class="avatar" role="img" aria-label="Portrait of legal assistant Clara Benton" style="background:radial-gradient(circle at 50% 40%,#d6c5b8,#6f7277)"></div><h4>Clara Benton</h4><p>Legal assistant</p></div>

<!-- quote -->
<div class="abs" role="img" aria-label="Dark car wreck scene behind the quote" style="left:0;top:2110px;width:1200px;height:376px;background:radial-gradient(ellipse at 60% 30%,rgba(180,90,50,.25),transparent 60%)"></div>
<svg class="abs" style="left:562px;top:2169px" width="74" height="74" viewBox="0 0 74 74"><circle cx="37" cy="37" r="37" fill="var(--white)"/><path d="M20 44c0-10 4-16 12-18l1 4c-4 2-6 5-6 8h5v10h-12zM39 44c0-10 4-16 12-18l1 4c-4 2-6 5-6 8h5v10h-12z" fill="var(--red)"/></svg>
<p class="quote">“Speak up for those who cannot speak for themselves, for<br>the rights of all who are destitute. Speak up and judge fairly;<br>defend the rights of the poor and needy.”</p>
<div class="abs" role="img" aria-label="Video still of a woman holding her neck beside a crashed car" style="left:262px;top:2388px;width:676px;height:337px;background:linear-gradient(120deg,#4c6b8a,#c9c5bd 45%,#b77444 62%,#7b8a6b)"></div>
<svg class="abs" style="left:576px;top:2533px" width="46" height="46" viewBox="0 0 46 46"><circle cx="23" cy="23" r="23" fill="var(--white)"/><path d="M19 15l12 8-12 8z" fill="var(--red)"/></svg>

<!-- testimonials -->
<h2 class="h2" style="top:2788px;left:-14px">TESTIMONIALS</h2>
<div class="t-card"></div>
<svg class="abs" style="left:958px;top:2837px" width="62" height="62"><circle cx="31" cy="31" r="31" fill="var(--red)"/></svg>
<svg class="abs" style="left:185px;top:2884px" width="160" height="150">
  <circle cx="128" cy="37" r="21" fill="#cfcfcf"/>
  <circle cx="21" cy="80" r="21" fill="#555"/>
  <circle cx="135" cy="113" r="21" fill="var(--red)"/>
</svg>
<div class="abs" role="img" aria-label="Client portrait" style="left:210px;top:2896px;width:122px;height:122px;border-radius:50%;background:radial-gradient(circle at 50% 40%,#e6e3df,#9b7a66)"></div>
<div class="abs" role="img" aria-label="Client portrait" style="left:84px;top:2912px;width:70px;height:70px;border-radius:50%;border:3px solid var(--pink);background:radial-gradient(circle,#c7a48d,#6e5747)"></div>
<div class="abs" role="img" aria-label="Client portrait" style="left:1032px;top:2908px;width:78px;height:78px;border-radius:50%;border:3px solid var(--pink);background:radial-gradient(circle,#d9c2b0,#6c8399)"></div>
<div class="t-name">Alan Brooks</div>
<p class="t-text">Lorem Ipsum is simply dummy text of the printing and typesetting industry. Lorem Ipsum has been the industry's standard dummy text ever since the 1500s, when an unknown printer took a galley of type and scrambled it to make a type specimen book.</p>

<!-- news -->
<h2 class="h2" style="top:3195px;color:var(--white)">LETEST NEWS</h2>
<article class="news" style="left:141px"><div class="thumb" role="img" aria-label="Semi-truck parked at dusk" style="background:linear-gradient(120deg,#2f3440,#7c8594 55%,#c9a99a)"></div><div class="date">July 1, 2019</div><h3>Trucking Company Offers 6 Figure Settlement</h3><p>On a Thursday afternoon, our client was traveling to work when suddenly a semi-truck</p></article>
<article class="news" style="left:449px"><div class="thumb" role="img" aria-label="Woman sitting on the road after a car collision" style="background:linear-gradient(120deg,#4f6a3e,#9aa89a 50%,#3f4245)"></div><div class="date">October 1, 2018</div><h3>County Agency Chooses to Dismiss Case</h3><p>In a case in Nashville, Davidson County, the county family services office was .</p></article>
<article class="news" style="left:756px"><div class="thumb" role="img" aria-label="Drivers on the phone beside crashed cars" style="background:linear-gradient(120deg,#c7ccd2,#8a9097 50%,#d07a3a)"></div><div class="date">October 1, 2018</div><h3>Pollard Obtains Jury</h3><p>In 2016, a client was traveling down a road and stopped in traffic when she was hit by another .</p></article>

<!-- contact -->
<h2 class="h2" style="top:3712px">CONTACT US</h2>
<div class="abs" role="img" aria-label="Faint world map" style="left:297px;top:3773px;width:611px;height:332px;background:radial-gradient(ellipse at center,var(--blush) 0%,rgba(252,237,238,.6) 55%,transparent 75%)"></div>
<div class="field" style="left:311px;top:3820px;width:268px">First Name :</div>
<div class="field" style="left:615px;top:3820px;width:272px">Last Name :</div>
<div class="field" style="left:311px;top:3873px;width:268px">Email :</div>
<div class="field" style="left:615px;top:3873px;width:272px">Phone No :</div>
<div class="field" style="left:311px;top:3941px;width:576px;padding-bottom:44px">Message :</div>
<div class="btn" style="left:540px;top:4023px;width:120px;height:35px">Read more</div>

<!-- footer -->
<div class="brand" style="top:4232px"><span class="mark"></span>Pollard Law Firm</div>
<div class="f-title" style="left:337px">Site Map</div>
<ul class="f-links"><li>- Home</li><li>- About Us</li><li>- Prectice Area</li><li>- Our Team</li><li>- News</li><li>- Contact Us</li></ul>
<div class="f-title" style="left:613px">Contact Us</div>
<svg class="f-icon" style="top:4262px" width="18" height="22" viewBox="0 0 18 22"><path d="M9 1a7 7 0 0 0-7 7c0 5 7 13 7 13s7-8 7-13a7 7 0 0 0-7-7z" fill="none" stroke="var(--red)" stroke-width="1.8"/><circle cx="9" cy="8" r="2.5" fill="var(--red)"/></svg>
<div class="f-item" style="top:4256px;width:220px">1450 Maple Crest Drive | Suite 210 | Franklin, TN 37000</div>
<svg class="f-icon" style="top:4328px" width="20" height="14" viewBox="0 0 20 14"><rect x="1" y="1" width="18" height="12" fill="none" stroke="var(--red)" stroke-width="1.8"/><path d="M1 1l9 7 9-7" fill="none" stroke="var(--red)" stroke-width="1.8"/></svg>
<div class="f-item" style="top:4325px">office@pollardlawfirm-example.com</div>
<svg class="f-icon" style="top:4380px" width="18" height="18" viewBox="0 0 18 18"><path d="M4 1l3 4-2 2c1 2 3 4 5 5l2-2 4 3-2 3C8 16 2 10 1 4z" fill="var(--red)"/></svg>
<div class="f-item" style="top:4380px">(615) 555-0142</div>
<div class="f-title" style="left:889px">Follow Us</div>
<div class="social" role="img" aria-label="Social profile link" style="left:887px"></div>
<div class="social" role="img" aria-label="Social profile link" style="left:923px"></div>
<div class="social" role="img" aria-label="Social profile link" style="left:959px"></div>
<div class="social" role="img" aria-label="Social profile link" style="left:995px"></div>
<div class="copy">©2021 Pollard Law Firm, PLLC. &nbsp;All Rights Reserved.</div>

</body>
</html>
```